Velvet Harbor for sale at the 2019 Tandor Crest Mare Auction on 30 May 2019

I am selling my broodmare at the 2019 Tandor Crest Mare auction on 30 May 2019. I need a flyer to hand out to potential buyers. I have included the required information in the attached word document. I can provide more images if required. I am thinking that a DL double sided or an A5 will suit best. I'm happy to provide more information as required.

Target Market(s)

Race horse breeders, people who buy broodmares.

Font styles to use
Serif
Sans Serif
Script

Colors

Designer to choose colors to be used in the design.

Requirements
Must have
• All of the content provided in the attached brief, however it is not necessary to have the words exactly as per the brief. The brief is for information purposes.
Nice to have
• Innovation...

```html
<!DOCTYPE html>
<html lang="en">
<head>
<meta charset="utf-8">
<title>Velvet Harbor – Sale Flyer</title>
<link rel="stylesheet" href="https://fonts.googleapis.com/css2?family=Alike&family=Roboto+Condensed:wght@400;700&display=swap">
<style>
  :root {
    --page-bg: #e6e6e6;
    --panel-dark: #1a090a;
    --panel-glow: #3a0d10;
    --red: #d0141c;
    --red-deep: #a50d14;
    --white: #ffffff;
    --silver: #e4e4e4;
    --turf: #5fa83a;
    --turf-dark: #3f7f28;
    --sky: #bcd6ea;
    --ghost: rgba(255, 255, 255, 0.07);
  }
  * { box-sizing: border-box; margin: 0; padding: 0; }
  html, body { width: 1200px; height: 1200px; overflow: hidden; }
  body {
    background: var(--page-bg);
    font-family: "Roboto Condensed", "Arial Narrow", sans-serif;
    color: var(--white);
    position: relative;
  }
  .flyer-side {
    position: absolute;
    top: 51px;
    width: 487px;
    height: 1035px;
    overflow: hidden;
    background:
      radial-gradient(ellipse at 50% 10%, var(--panel-glow) 0%, transparent 60%),
      radial-gradient(ellipse at 50% 90%, var(--panel-glow) 0%, transparent 55%),
      var(--panel-dark);
  }
  .flyer-front { left: 81px; }
  .flyer-back { left: 640px; }
  .abs { position: absolute; }

  /* Front */
  .horse-name {
    left: 40px; top: 38px;
    font-family: "Alike", Georgia, serif;
    font-size: 62px; line-height: 66px;
    color: var(--silver);
    text-align: center;
    letter-spacing: 1px;
    text-shadow: 0 2px 0 #7a7a7a;
  }
  .lot-tab { left: 367px; top: 50px; width: 120px; height: 100px; }
  .lot-tab svg { position: absolute; inset: 0; }
  .lot-label {
    position: absolute; left: 0; right: 0; top: 20px;
    text-align: center; font-size: 20px;
  }
  .lot-number {
    position: absolute; left: 0; right: 0; top: 42px;
    text-align: center; font-size: 40px; font-weight: 700;
  }
  .sale-box {
    left: 26px; top: 197px; width: 435px; height: 201px;
    border: 2px solid var(--red);
  }
  .stable-row {
    height: 56px; display: flex; align-items: center; justify-content: center; gap: 12px;
    font-size: 22px;
  }
  .stable-code { color: var(--red); font-size: 40px; font-weight: 700; }
  .date-row {
    height: 60px; margin: 0 -2px; background: var(--red);
    display: flex; align-items: center; justify-content: center; gap: 12px;
    font-size: 23px;
  }
  .sale-date { font-size: 44px; font-weight: 700; }
  .sale-row {
    padding-top: 10px; text-align: center; font-size: 30px; font-weight: 700; line-height: 32px;
  }
  .sale-row small { color: var(--red); font-size: 16px; font-weight: 400; }
  .race-record { left: 0; right: 0; top: 422px; text-align: center; }
  .race-record .label { color: var(--red); font-size: 17px; }
  .race-record .stats { font-size: 22px; margin-top: 4px; }
  .race-record .prize { color: var(--red); font-size: 32px; font-weight: 700; line-height: 36px; }
  .pedigree {
    left: 30px; right: 30px; top: 521px;
    text-align: center; font-size: 16.5px; line-height: 24px;
  }
  .pedigree .sire { color: var(--red); }
  .hero-band { left: 0; top: 637px; width: 487px; height: 264px; }
  .caption { text-align: center; }
  .caption .headline { color: var(--red); font-weight: 700; }
  .front-caption { left: 0; right: 0; top: 930px; font-size: 18px; line-height: 23px; }
  .front-caption .headline { font-size: 21px; }

  /* Back */
  .ghost-name {
    left: 66px; top: 518px;
    transform: translate(-50%, -50%) rotate(-90deg);
    font-family: "Alike", Georgia, serif;
    font-size: 112px; line-height: 1;
    color: var(--ghost);
    white-space: nowrap;
  }
  .race-photo {
    left: 164px; width: 294px; height: 163px;
    border-radius: 0 34px 0 34px;
    background: linear-gradient(to bottom, var(--sky) 0%, #9fb2a4 40%, var(--turf) 55%, var(--turf-dark) 100%);
  }
  .race-photo.photo-screen {
    background: linear-gradient(to bottom, #dfe6ea 0%, #4c8a3a 20%, #2f5e22 45%, var(--turf) 62%, var(--turf-dark) 100%);
  }
  .back-caption { left: 150px; width: 322px; font-size: 14px; line-height: 20px; }
  .back-caption .headline { font-size: 16px; }
</style>
</head>
<body>

<section class="flyer-side flyer-front">
  <h1 class="abs horse-name">VELVET<br>HARBOR</h1>

  <div class="abs lot-tab">
    <svg viewBox="0 0 120 100" aria-hidden="true">
      <polygon points="0,8 120,0 120,100 0,100 10,54" fill="var(--red)"/>
      <polygon points="0,8 12,0 120,0 120,8" fill="var(--red-deep)"/>
    </svg>
    <div class="lot-label">LOT NO:</div>
    <div class="lot-number">1414</div>
  </div>

  <div class="abs sale-box">
    <div class="stable-row"><span>STABLE:</span><span class="stable-code">QC 6</span></div>
    <div class="date-row"><span>SALE DATE:</span><span class="sale-date">30 MAY 2019</span></div>
    <div class="sale-row"><small>SALE : </small>2019 TANDOR CREST<br>MARE AUCTION</div>
  </div>

  <div class="abs race-record">
    <div class="label">RACE RECORD :</div>
    <div class="stats">7 WINS, 2 SECONDS,&nbsp; 2 THIRDS (27-7:2:2),</div>
    <div class="prize">$205,400 PRIZEMONEY</div>
  </div>

  <p class="abs pedigree">In foal to <span class="sire">FAR MEADOW</span>, sire of: Starlit Surge (winner of the Group 3 Lagoon Bay Stakes by 7.5L), Delve Down (winner of the Group 2 Westmere Plate), Gale Runner (winner of the Tandor Crest Clockwise Classic), Swift Arrow, Copper Nova plus more...</p>

  <svg class="abs hero-band" viewBox="0 0 487 264" aria-hidden="false">
    <polygon points="0,0 243,22 487,0 487,10 243,32 0,10" fill="var(--red)"/>
    <defs>
      <linearGradient id="heroTones" x1="0" y1="0" x2="0" y2="1">
        <stop offset="0" stop-color="#dfe4e6"/>
        <stop offset="0.18" stop-color="#6cbf4a"/>
        <stop offset="0.45" stop-color="#3f8a2c"/>
        <stop offset="0.6" stop-color="#5fae3e"/>
        <stop offset="1" stop-color="#4a9a32"/>
      </linearGradient>
    </defs>
    <polygon role="img" aria-label="Photo: Velvet Harbor winning at Kestrel Park in front of the big screen"
      points="0,10 243,32 487,10 487,228 243,240 0,228" fill="url(#heroTones)"/>
    <polygon points="0,228 243,240 487,228 487,242 243,264 0,242" fill="var(--red)"/>
  </svg>

  <div class="abs caption front-caption">
    <div class="headline">Velvet Harbor wins by 3.5L</div>
    <div>Class 6 Handicap – 1400m</div>
    <div>Riverbend Racing Club (Kestrel Park),21 January 2017</div>
  </div>
</section>

<section class="flyer-side flyer-back">
  <div class="abs ghost-name" aria-hidden="true">VELVET HARBOR</div>

  <div class="abs race-photo photo-screen" style="top:27px" role="img" aria-label="Photo: Velvet Harbor winning at Kestrel Park"></div>
  <div class="abs caption back-caption" style="top:202px">
    <div class="headline">Velvet Harbor wins by 2.8L</div>
    <div>No More Than One Metro Win Handicap – 1400m</div>
    <div>Riverbend Racing Club (Kestrel Park), 10 December 2016</div>
  </div>

  <div class="abs race-photo photo-screen" style="top:278px" role="img" aria-label="Photo: Velvet Harbor leading the field to the line at Kestrel Park"></div>
  <div class="abs caption back-caption" style="top:453px">
    <div class="headline">Velvet Harbor beats Silver Quay by 1.3L</div>
    <div>Class 6 Plate – 1300m</div>
    <div>Riverbend Racing Club (Kestrel Park), 29 April 2017</div>
  </div>

  <div class="abs race-photo" style="top:529px" role="img" aria-label="Photo: Velvet Harbor winning at Dunmore"></div>
  <div class="abs caption back-caption" style="top:701px">
    <div class="headline">Velvet Harbor wins by 2.3L</div>
    <div>Class 4 Handicap – 1400m</div>
    <div>Riverbend Racing Club (Dunmore), 23 November 2016</div>
  </div>

  <div class="abs race-photo" style="top:778px" role="img" aria-label="Photo: Velvet Harbor winning on debut at the Bayside Coast"></div>
  <div class="abs caption back-caption" style="top:950px">
    <div class="headline">Velvet Harbor wins on debut at the Bayside Coast!</div>
    <div>Maiden – 1000m</div>
    <div>Bayside Coast Turf Club, 23 October 2015</div>
  </div>
</section>

</body>
</html>
```